Web Design Project

We need web design for a new baby products (nursery furniture) business in Australia.

The logo is already done, and I would like to reflect a similar theme throughout the website:
* Clean, white background.
* Use of lime green, purple and orange.
* Similar font to logo for headings
* FUNKY, FASHIONABLE, QUALITY feeling of website.

The main concept is to be attractive to discerning mums who are buying big items like a cot or chest of drawers. These are expensive items and will be considered the most important purchases for a newborn, so the website has to be enticing!!!
Updates

Hello,

Thank you for your submissions. I have received a few questions regarding the font and the coding of this website.

The job I am seeking is for design for an E-commerce store. The font was done by another craft hive designer, so I do not know what type of font I am sorry.

I was hoping to have more designs by now, so please send them soon, this project is guaranteed!

I also ask you to read the brief properly please. The name of the business is Cradle Lane, as the logo says. The use of design that I have mentioned has only been demonstrated in a couple of designs submitted to me.

I look forward to seeing your work soon!

Kind Regards
Marla

Target Market(s)

Young mothers aged 25-45

Industry/Entity Type

Business

Requirements
Must have
• Must be funky, bright, energetic, attractive visually.
Nice to have
• I like the idea of some floral / design work in faded lime green, purple on some of the edges of different pages. Maybe islamic design? But has to be very fashionable.
Should not have
• Should not have any traditional ideas of baby websites.

ie- no stork, nappy images, teddybears etc.

```html
<!DOCTYPE html>
<html lang="en">
<head>
<meta charset="utf-8">
<title>Cradle Lane</title>
<link rel="stylesheet" href="https://fonts.googleapis.com/css2?family=Fredoka:wght@600&family=Arimo:wght@400;700&family=PT+Sans+Narrow&display=swap">
<style>
:root{
  --lime:#8ecf0b;
  --lime-dark:#6fa908;
  --purple:#b83ad1;
  --nav-dark:#5e056c;
  --orange:#f7941d;
  --page:#ececec;
  --line:#dcdcdc;
  --text:#333;
  --muted:#888;
  --price:#b83ad1;
  --display:"Fredoka","Arial Rounded MT Bold",sans-serif;
}
*{box-sizing:border-box;margin:0;padding:0}
html,body{width:1200px;height:1031px;overflow:hidden}
body{background:var(--page);font-family:"Arimo",Arial,sans-serif;color:var(--text);position:relative}
a{color:inherit;text-decoration:none}
.abs{position:absolute}

.topbar{left:0;top:0;width:1200px;height:27px;background:var(--lime);border-bottom:3px solid var(--lime-dark);color:#fff;font-size:12px}
.topbar .welcome{left:101px;top:6px}
.topbar .links{right:100px;top:6px;word-spacing:2px}
.topbar .links span{margin:0 9px}

.header{left:99px;top:30px;width:1001px;height:131px;background:#fff}
.contact-line{left:26px;top:59px;width:318px;height:1px;background:var(--line)}
.phone{left:78px;top:16px;display:flex;align-items:center;gap:14px;font-size:12px;color:#555}
.social{left:88px;top:86px;display:flex;gap:21px}
.social i{display:block;width:20px;height:20px;border-radius:50%;background:#222}
.divider{top:12px;width:1px;height:102px;background:var(--line)}
.brand{left:370px;top:40px;display:flex;align-items:center;gap:12px}
.brand .dot{width:48px;height:48px;border-radius:50%;background:var(--lime)}
.brand .name{font-family:var(--display);font-weight:600;font-size:38px;color:var(--purple);white-space:nowrap}
.cart-line{left:664px;top:59px;width:318px;height:1px;background:var(--line)}
.mini-cart{left:684px;top:14px;display:flex;align-items:center;gap:8px;font-size:12px;color:#555}
.mini-cart b{font-size:17px;color:#222;font-weight:700;margin-left:4px}
.search{left:684px;top:72px;width:280px;height:38px;border:1px solid #ddd;border-radius:6px;box-shadow:inset 0 1px 3px rgba(0,0,0,.1);font-size:12px;color:#555;padding:10px 17px}
.search svg{position:absolute;right:14px;top:9px}

.nav{left:99px;top:161px;width:1001px;height:42px;background:linear-gradient(#8b1a9b,var(--nav-dark));border-bottom:3px solid var(--orange);display:flex;font-family:"PT Sans Narrow",sans-serif;font-size:17px;color:#fff;letter-spacing:.5px}
.nav a{display:block;padding:10px 0 0 20px;height:39px;border-right:1px solid rgba(255,255,255,.25)}

.hero{left:99px;top:216px;width:742px;height:415px;background:#fff;border:1px solid var(--line);overflow:hidden}
.hero .photo{left:24px;top:70px;width:370px;height:310px;border-radius:30px;background:linear-gradient(90deg,#5a3a24,#f3f3f0 35%,#fff 80%,#6b4a30)}
.hero .headline{font-family:var(--display);font-weight:600;white-space:nowrap;line-height:1}
.hero .t1{left:406px;top:6px;font-size:90px;color:var(--purple);letter-spacing:-2px}
.hero .t2{left:404px;top:118px;font-size:118px;color:var(--lime);letter-spacing:-3px}
.hero .t3{left:406px;top:250px;font-size:56px;color:var(--orange);letter-spacing:-1px}
.shop{left:409px;top:320px;width:175px;height:42px;border-radius:5px;background:linear-gradient(#4a4a4a,#1c1c1c);color:#fff;font-weight:700;font-size:17px;display:flex;align-items:center;gap:12px;padding-left:18px}
.dots{left:592px;top:378px;display:flex;gap:6px}
.dots i{width:20px;height:20px;border-radius:50%;background:var(--lime);border:2px solid #fff;box-shadow:0 0 0 1px #6fa908}
.dots i.on{background:var(--orange);box-shadow:0 0 0 2px #7a0d8a}

.tile{left:846px;width:254px;height:126px;background:#fff;border:1px solid var(--line);padding:2px}
.tile .photo{width:100%;height:100%}
.tile .tag{font-family:var(--display);font-weight:600;color:#fff;white-space:nowrap}
.tag-new{right:14px;top:14px;width:66px;height:66px;border-radius:50%;background:var(--lime);border:3px solid #fff;font-size:22px;display:flex;align-items:center;justify-content:center}
.tag-offer{right:3px;top:12px;background:var(--purple);font-size:21px;line-height:1.15;padding:2px 6px;width:106px;white-space:normal!important}
.tag-count{left:12px;bottom:6px;color:var(--orange)!important;font-size:23px}

.featured{left:99px;top:645px;width:1001px;height:292px;background:#fff;border:1px solid var(--line)}
.featured h2{left:32px;top:12px;height:34px;padding:0 10px;background:var(--purple);color:#fff;font-family:var(--display);font-weight:600;font-size:18px;line-height:34px;white-space:nowrap}
.stripe{left:210px;top:26px;width:762px;height:7px;background:repeating-linear-gradient(-45deg,var(--lime) 0 2px,#fff 2px 4px)}
.product{top:57px;width:208px}
.product .title{font-size:12px;color:#222}
.product .thumb{margin-top:8px;width:208px;height:146px;border:1px solid var(--line);padding:3px;position:relative}
.product .img{width:100%;height:100%}
.product .meta{margin-top:10px;display:flex;justify-content:space-between;font-size:12px;color:var(--muted)}
.product .meta b{font-weight:400;color:var(--price);font-size:14px}
.product .acts{margin-top:8px;display:flex;justify-content:space-between;align-items:center}
.save{right:8px;top:12px;width:66px;height:66px;border-radius:50%;background:var(--orange);border:2px dashed #fff;color:#fff;font-family:var(--display);font-weight:600;font-size:17px;line-height:1.05;text-align:center;padding-top:13px}
.arrow{top:760px;width:32px;height:70px;background:#fff;border:1px solid var(--line);display:flex;align-items:center;justify-content:center}
.arrow.left{left:92px;border-radius:0 35px 35px 0}
.arrow.right{left:1077px;border-radius:35px 0 0 35px}

.footer{left:97px;width:1004px;font-size:12px;color:#444}
.footer b{color:#222}
.footer .copy{right:0;top:0}
</style>
</head>
<body>

<div class="abs topbar">
  <span class="abs welcome">Welcome Message</span>
  <span class="abs links">My Account<span>|</span>My Wishlist<span>|</span>My Cart<span>|</span>Checkout<span>|</span>Site Map</span>
</div>

<header class="abs header">
  <div class="abs phone">
    <svg width="40" height="28" viewBox="0 0 40 28"><path d="M4 10c8-8 24-8 32 0l-4 4-5-3v-3H13v3l-5 3z" fill="#d33"/><rect x="9" y="14" width="22" height="12" rx="3" fill="#c22"/><circle cx="20" cy="20" r="4" fill="#fff"/></svg>
    <span>Toll Free: 000-000-00000</span>
  </div>
  <div class="abs contact-line"></div>
  <div class="abs social"><i></i><i></i><i></i><i></i><i></i></div>
  <div class="abs divider" style="left:344px"></div>
  <div class="abs brand"><span class="dot"></span><span class="name">Cradle Lane</span></div>
  <div class="abs divider" style="left:663px"></div>
  <div class="abs mini-cart">
    <span>My Cart</span>
    <svg width="30" height="30" viewBox="0 0 30 30"><path d="M2 6h5l4 15h14l3-11H9" fill="none" stroke="#6a8aa8" stroke-width="2"/><circle cx="13" cy="26" r="2" fill="#6a8aa8"/><circle cx="23" cy="26" r="2" fill="#6a8aa8"/></svg>
    <b>$0.00</b>
  </div>
  <div class="abs cart-line"></div>
  <div class="abs search">Search site here
    <svg width="22" height="20" viewBox="0 0 22 20"><circle cx="8" cy="8" r="6" fill="none" stroke="#111" stroke-width="2.5"/><path d="M12.5 12.5l7 6" stroke="#111" stroke-width="3"/></svg>
  </div>
</header>

<nav class="abs nav">
  <a style="width:88px">HOME</a>
  <a style="width:150px">ABOUT US</a>
  <a style="width:143px">PRODUCTS</a>
  <a style="width:110px">FAQS</a>
  <a style="width:142px">SPECIALS</a>
  <a style="border:0">CONTACT US</a>
</nav>

<section class="abs hero">
  <div class="abs photo" role="img" aria-label="Modern wooden cot with white slats and mattress"></div>
  <div class="abs headline t1">biggest</div>
  <div class="abs headline t2">EVER</div>
  <div class="abs headline t3">collection</div>
  <a class="abs shop">
    <svg width="26" height="22" viewBox="0 0 26 22"><path d="M1 3h4l3 11h13l3-8H7" fill="none" stroke="#fff" stroke-width="2"/><circle cx="10" cy="19" r="2" fill="#fff"/><circle cx="19" cy="19" r="2" fill="#fff"/></svg>
    SHOP NOW</a>
  <div class="abs dots"><i class="on"></i><i></i><i></i><i></i></div>
</section>

<div class="abs tile" style="top:216px">
  <div class="photo" role="img" aria-label="Light wood cot in a pale blue room" style="background:linear-gradient(#c9ddea,#e8ded2 70%,#d7b596)"></div>
  <div class="abs tag tag-new">NEW</div>
</div>
<div class="abs tile" style="top:359px">
  <div class="photo" role="img" aria-label="Nursery furniture set with wardrobe and drawers" style="background:linear-gradient(#8fb8dc,#d6d8d2 60%,#b9a58c)"></div>
  <div class="abs tag tag-offer">Exclusive offers</div>
</div>
<div class="abs tile" style="top:502px">
  <div class="photo" role="img" aria-label="Wooden cot beside a bright window" style="background:linear-gradient(#d9e9ec,#efe6da 70%,#c8a784)"></div>
  <div class="abs tag tag-count">Over 500 Products</div>
</div>

<svg width="0" height="0" style="position:absolute"><defs><path id="s" d="M8 0l2.4 5 5.5.7-4 3.8 1 5.5L8 12.3 3.1 15l1-5.5-4-3.8 5.5-.7z"/><g id="cart"><path d="M1 2h4l3 9h10l2-6H6" fill="none" stroke="#333" stroke-width="2"/><circle cx="9" cy="15" r="2" fill="#333"/><circle cx="17" cy="15" r="2" fill="#333"/><path d="M23 12h5M25.5 9.5v5" stroke="#333"/></g></defs></svg>

<section class="abs featured">
  <h2 class="abs">Featured Products</h2>
  <div class="abs stripe"></div>

  <div class="abs product" style="left:32px">
    <div class="title">Vivamus eget viverra turpis</div>
    <div class="thumb"><div class="img" role="img" aria-label="Carved lattice folding screen" style="background:linear-gradient(90deg,#eee,#b89a70 25%,#a98c66 75%,#ddd)"></div></div>
    <div class="meta"><span>VG2T0618A-RED</span><b>$200.00</b></div>
    <div class="acts">
      <svg width="30" height="18" viewBox="0 0 30 18"><use href="#cart"/></svg>
      <svg width="90" height="16" viewBox="0 0 90 16"><use href="#s" fill="#333"/><use href="#s" x="18" fill="#333"/><use href="#s" x="36" fill="#333"/><use href="#s" x="54" fill="#ccc"/><use href="#s" x="72" fill="#ccc"/></svg>
    </div>
  </div>

  <div class="abs product" style="left:277px">
    <div class="title">Vivamus eget viverra turpis</div>
    <div class="thumb"><div class="img" role="img" aria-label="Nursery dresser and wardrobe in a blue room" style="background:linear-gradient(#7fb2da,#cfd4d0 60%,#d9c3a5)"></div><div class="abs save">save<br>20%</div></div>
    <div class="meta"><span>VG2T0618A-RED</span><b>$200.00</b></div>
    <div class="acts">
      <svg width="30" height="18" viewBox="0 0 30 18"><use href="#cart"/></svg>
      <svg width="90" height="16" viewBox="0 0 90 16"><use href="#s" fill="#333"/><use href="#s" x="18" fill="#333"/><use href="#s" x="36" fill="#333"/><use href="#s" x="54" fill="#ccc"/><use href="#s" x="72" fill="#ccc"/></svg>
    </div>
  </div>

  <div class="abs product" style="left:519px">
    <div class="title">Vivamus eget viverra turpis</div>
    <div class="thumb"><div class="img" role="img" aria-label="White cot with blue drawers and toys" style="background:linear-gradient(#fff,#f1f4f8 55%,#9cc2e6)"></div></div>
    <div class="meta"><span>VG2T0618A-RED</span><b>$200.00</b></div>
    <div class="acts">
      <svg width="30" height="18" viewBox="0 0 30 18"><use href="#cart"/></svg>
      <svg width="90" height="16" viewBox="0 0 90 16"><use href="#s" fill="#333"/><use href="#s" x="18" fill="#333"/><use href="#s" x="36" fill="#333"/><use href="#s" x="54" fill="#ccc"/><use href="#s" x="72" fill="#ccc"/></svg>
    </div>
  </div>

  <div class="abs product" style="left:765px">
    <div class="title">Vivamus eget viverra turpis</div>
    <div class="thumb"><div class="img" role="img" aria-label="Carved lattice folding screen" style="background:linear-gradient(90deg,#eee,#b89a70 25%,#a98c66 75%,#ddd)"></div></div>
    <div class="meta"><span>VG2T0618A-RED</span><b>$200.00</b></div>
    <div class="acts">
      <svg width="30" height="18" viewBox="0 0 30 18"><use href="#cart"/></svg>
      <svg width="90" height="16" viewBox="0 0 90 16"><use href="#s" fill="#333"/><use href="#s" x="18" fill="#333"/><use href="#s" x="36" fill="#333"/><use href="#s" x="54" fill="#ccc"/><use href="#s" x="72" fill="#ccc"/></svg>
    </div>
  </div>
</section>

<a class="abs arrow left"><svg width="14" height="16" viewBox="0 0 14 16"><path d="M11 2L4 8l7 6" fill="none" stroke="#7cc30a" stroke-width="4"/></svg></a>
<a class="abs arrow right"><svg width="14" height="16" viewBox="0 0 14 16"><path d="M3 2l7 6-7 6" fill="none" stroke="#7cc30a" stroke-width="4"/></svg></a>

<footer>
  <div class="abs footer" style="top:955px"><b>Links</b>: Home &nbsp;|&nbsp; About Us &nbsp;|&nbsp; Products &nbsp;|&nbsp; Faqs &nbsp;|&nbsp; Contact Us
    <span class="abs copy">Copyright © 2012 Cradle Lane. All rights reserved.</span></div>
  <div class="abs footer" style="top:985px"><b>Info</b>: Gift Voucher &nbsp;| Customer Feedback | Terms &amp; Conditions | Privacy Policy</div>
</footer>

</body>
</html>
```